Innovation Company Business Card Design

I need to have my business card updated. The current card was designed when the company started 2.5 years ago and was a quick and dirty job.

I need a new card design that is more professional and has my updated company tag line.

I will include the old card's Corel Draw file, and EPS versions as examples of the current design. I will also include the company logo eps and corel version files.

The company pantone colour is pantone 1805 c (a dark red)

I want the design to convey the nature of our business as a strategic technology innovation company, but yet still be professional. We are funky vibey and work from an industrial style office in a vibey designer dominat part of town. Though are clients include large banks and corporate clients too.

The information that needs to be on the card is in attached word document (but doesn't have to be in this order or format)

Final version needs to be supplied in PNG preview, as well as PSD file format (or other editable file version) so that personal information on card can be easily edited and reprinted.

Target Market(s)

CEO's of small to medium size companies
Marketing Managers of large coporates
Account managers of Digital Agencies

Industry/Entity Type

Business

Requirements
Must have
• 86x54mm will be cut in rounded corner credit card size format (Except if you recommend otherwise in your design)
Nice to have
• Some kind of background transparency combined with the pantone colour that gives the card some dimension and depth. But no gradient fills please :-)
Should not have
• Basic gradient fills
• Clipart

```html
<!DOCTYPE html>
<html lang="en">
<head>
<meta charset="utf-8">
<title>Novaquill Business Card</title>
<link rel="stylesheet" href="https://fonts.googleapis.com/css2?family=Montserrat:wght@300;800&family=Roboto+Condensed:wght@400;700&display=swap">
<style>
  :root {
    --brand-red: #b8242f;
    --card-white: #f8f8f8;
    --card-charcoal: #4a4b4f;
    --ink: #1d1d1f;
    --ink-soft: #3a3a3c;
    --backdrop: #d9d9d9;
    --paper-white: #ffffff;
  }
  * { margin: 0; padding: 0; box-sizing: border-box; }
  html, body {
    width: 1200px;
    height: 1000px;
    overflow: hidden;
    background: var(--backdrop);
  }
  .stage {
    position: relative;
    width: 1200px;
    height: 1000px;
  }
  .card {
    position: absolute;
    top: 330px;
    width: 540px;
    height: 339px;
    border-radius: 22px;
    overflow: hidden;
  }
  .card--front { left: 40px; background: var(--card-white); }
  .card--back { left: 620px; background: var(--card-charcoal); }

  .brand-band {
    position: absolute;
    left: 0;
    top: 112px;
    width: 335px;
    height: 112px;
    background: var(--brand-red);
    display: flex;
    flex-direction: column;
    justify-content: center;
    padding-left: 40px;
  }
  .brand-name {
    font-family: "Montserrat", sans-serif;
    font-weight: 800;
    font-size: 40px;
    letter-spacing: -1px;
    color: var(--paper-white);
    line-height: 1;
  }
  .brand-tagline {
    font-family: "Montserrat", sans-serif;
    font-weight: 300;
    font-size: 13px;
    color: var(--paper-white);
    margin: 6px 0 0 104px;
    letter-spacing: 0.3px;
  }

  .contact-block {
    position: absolute;
    left: 355px;
    top: 122px;
    font-family: "Roboto Condensed", sans-serif;
    color: var(--ink);
  }
  .contact-name { font-weight: 700; font-size: 20px; line-height: 1.1; }
  .contact-role { font-size: 13px; color: var(--ink-soft); margin-top: 2px; }
  .contact-lines { margin-top: 20px; font-size: 13px; color: var(--ink-soft); }
  .contact-line { display: flex; gap: 14px; line-height: 1.6; }
  .contact-label { color: var(--brand-red); font-weight: 700; width: 8px; }

  .company-line {
    position: absolute;
    left: 26px;
    bottom: 26px;
    display: flex;
    align-items: center;
    font-family: "Roboto Condensed", sans-serif;
    font-size: 13.5px;
    color: var(--ink);
    white-space: nowrap;
  }
  .company-line .divider {
    width: 2px;
    height: 18px;
    background: var(--brand-red);
    margin: 0 8px;
  }

  .back-art { display: block; }
  .back-art text {
    font-family: "Montserrat", sans-serif;
    font-weight: 300;
    fill: var(--paper-white);
  }
</style>
</head>
<body>
<main class="stage">
  <section class="card card--front" aria-label="Business card front">
    <div class="brand-band">
      <span class="brand-name">Novaquill</span>
      <span class="brand-tagline">Strategic Innovation</span>
    </div>
    <div class="contact-block">
      <p class="contact-name">Daniel Harrow</p>
      <p class="contact-role">Founder &amp; MD</p>
      <div class="contact-lines">
        <p class="contact-line"><span class="contact-label">e</span><span>daniel@novaquill.com</span></p>
        <p class="contact-line"><span class="contact-label">m</span><span>082 475 3160</span></p>
      </div>
    </div>
    <p class="company-line">
      <span>Novaquill (Pty) Ltd</span><span class="divider"></span>
      <span>Suite 210, 14 Marlow Ave. Parkview, JHB, RSA</span><span class="divider"></span>
      <span>010 482 3317</span>
    </p>
  </section>

  <section class="card card--back" aria-label="Business card back">
    <svg class="back-art" width="540" height="339" viewBox="0 0 540 339">
      <rect width="540" height="339" fill="var(--card-charcoal)" role="img" aria-label="Subtle repeating brand-mark texture on charcoal"/>
      <g transform="translate(200,250) rotate(-45)">
        <rect class="mark-square" x="-64" y="-14" width="56" height="56" fill="var(--brand-red)"/>
        <rect class="stripe" x="0" y="0" width="420" height="48" fill="var(--brand-red)"/>
        <rect class="stripe" x="40" y="60" width="420" height="48" fill="var(--brand-red)"/>
        <text x="22" y="35" font-size="30">Strategic</text>
        <text x="62" y="95" font-size="30">Innovation</text>
      </g>
    </svg>
  </section>
</main>
</body>
</html>
```